I need business cards for a company that will be an umbrella for many retail stores. I need them to be sleek and modern. I would like some white and black in the background of the card as these are the office colours the logo is attached.
Target Market(s)
worldwide
Industry/Entity Type
Business
Requirements
Must have
- traditional business card shape
Should not have
- too many colours
no swirly text

```html
<!DOCTYPE html>
<html lang="en">
<head>
<meta charset="utf-8">
<title>NORRA General Trading – Business Card</title>
<link rel="stylesheet" href="https://fonts.googleapis.com/css2?family=Cinzel:wght@400;600;700&display=swap">
<style>
  :root {
    --brand-blue: #2c5f9b;
    --brand-blue-soft: #adb9d6;
    --paper: #ffffff;
    --ink: #1f1f1f;
    --label-ink: #111111;
  }
  * { margin: 0; padding: 0; box-sizing: border-box; }
  html, body {
    width: 905px;
    height: 1200px;
    overflow: hidden;
    background: var(--paper);
  }
  .sheet {
    position: relative;
    width: 685px;
    height: 908px;
    transform: scale(1.3212);
    transform-origin: 0 0;
  }
  .card {
    position: absolute;
    left: 80px;
    width: 526px;
    overflow: hidden;
  }
  .card--front { top: 50px; height: 300px; background: var(--paper); }
  .card--back { top: 505px; height: 298px; background: var(--brand-blue-soft); }

  .band { position: absolute; left: 0; width: 100%; }
  .band--head { top: 0; height: 50px; background: var(--brand-blue); }
  .card--back .band--head { height: 47px; }
  .band--head-rule { top: 50px; height: 10px; background: var(--brand-blue-soft); }
  .band--foot-rule { top: 283px; height: 9px; background: var(--brand-blue-soft); }
  .band--foot { bottom: 0; height: 8px; background: var(--brand-blue); }
  .card--back .band--foot { height: 7px; }

  .holder-name {
    position: absolute;
    right: 10px;
    top: 10px;
    font-family: "Cinzel", serif;
    font-weight: 600;
    font-size: 25px;
    letter-spacing: 0.5px;
    color: var(--paper);
    line-height: 1;
  }
  .card--back .holder-name { top: 9px; }

  .company {
    position: absolute;
    font-family: "Cinzel", serif;
    font-weight: 400;
    color: var(--ink);
    line-height: 1;
  }
  .company__name { display: block; font-size: 41px; letter-spacing: 1px; }
  .company__line { display: block; font-size: 19px; letter-spacing: 0.6px; margin-top: 3px; }
  .card--front .company { left: 248px; top: 212px; }
  .card--back .company { left: 15px; top: 221px; }

  .contact {
    position: absolute;
    left: 309px;
    top: 80px;
    list-style: none;
    font-family: "Cinzel", serif;
    font-weight: 700;
    font-size: 21px;
    line-height: 27px;
    color: var(--ink);
  }

  .side-label {
    position: absolute;
    left: 0;
    width: 666px;
    text-align: center;
    font-family: Helvetica, Arial, sans-serif;
    font-size: 36px;
    color: var(--label-ink);
    line-height: 1;
  }
  .side-label--front { top: 384px; }
  .side-label--back { top: 824px; }
</style>
</head>
<body>
  <div class="sheet">
    <section class="card card--front">
      <div class="band band--head"></div>
      <div class="band band--head-rule"></div>
      <p class="holder-name">Daniel Marsh</p>
      <p class="company">
        <span class="company__name">NORRA</span>
        <span class="company__line">GENERAL TRADING</span>
      </p>
      <div class="band band--foot-rule"></div>
      <div class="band band--foot"></div>
    </section>
    <p class="side-label side-label--front">Front</p>

    <section class="card card--back">
      <div class="band band--head"></div>
      <p class="holder-name">Daniel Marsh</p>
      <ul class="contact">
        <li>Title</li>
        <li>Address</li>
        <li>(555)555-5555</li>
      </ul>
      <p class="company">
        <span class="company__name">NORRA</span>
        <span class="company__line">GENERAL TRADING</span>
      </p>
      <div class="band band--foot"></div>
    </section>
    <p class="side-label side-label--back">Back</p>
  </div>
</body>
</html>
```